Creative, eye-catching 1/4-page ad design

We are an Australian caravan manufacturer that requires an eye-catching 1/4-page advertisement for a digital magazine.
We would like our ad to include the following information:
- We specialise in light weight fibreglass composite caravans
- Our ad should emphasize that our caravans are Australian made and locally manufactured.
- We would like to see designs that use the colour blue (please refer to posts on our FB page)
- Photos can be found on our Facebook page.
Website: www.bluegumtrailers.com.au Facebook URL: https://www.facebook.com/bluegumtrailers

Target Market(s)

35-75 male & female

Industry/Entity Type

Caravan manufacturing

Font styles to use
Serif

Colors
0054AA
0677BA
7BADD7
CADEEF
E8F1F8
0094D4
00A9DD
6FCCEA
C7EBF8
E9F6FB

Requirements
Must have
• Contact details - can be found on Facebook page and webiste
Nice to have
• Caravan interior photos - please refer to FB page for an appropriate image that would suit your design

```html
<!DOCTYPE html>
<html lang="en">
<head>
<meta charset="utf-8">
<title>Bluegum Trailers – Quarter Page Ad</title>
<link href="https://fonts.googleapis.com/css2?family=Poppins:ital,wght@0,600;0,700;1,700;1,800;1,900&family=Oswald:wght@600&display=swap" rel="stylesheet">
<style>
  :root{
    --stage:#8f8f8f;
    --navy:#0c2d6b;
    --navy-deep:#081f52;
    --blue:#0054aa;
    --blue-mid:#0677ba;
    --sky:#0094d4;
    --sky-bright:#00a9dd;
    --sky-soft:#6fccea;
    --ice:#e9f6fb;
    --white:#ffffff;
    --ink:#1a1a1a;
  }
  html,body{margin:0;padding:0;}
  body{
    width:1200px;height:2234px;overflow:hidden;
    background:radial-gradient(circle at 50% 45%,#a9a9a9,var(--stage));
    position:relative;
    font-family:"Poppins",sans-serif;
  }
  .ad-frame{
    position:absolute;left:75px;top:424px;
    width:1050px;height:1386px;
    box-shadow:0 20px 50px rgba(0,0,0,.35);
  }
  .ad{
    position:absolute;left:0;top:0;
    width:600px;height:792px;
    transform:scale(1.75);transform-origin:0 0;
    background:var(--white);overflow:hidden;
  }
  .ad svg.backdrop{position:absolute;inset:0;}
  .brand{
    position:absolute;left:40px;top:30px;width:190px;
    display:flex;align-items:center;gap:10px;
  }
  .brand-mark{flex:none;width:16px;height:16px;border-radius:50%;background:var(--blue);}
  .brand-name{
    margin:0;font-weight:700;font-size:28px;line-height:32px;
    color:var(--blue);letter-spacing:.5px;
  }
  .divider{position:absolute;left:245px;top:20px;width:2px;height:86px;background:#cfcfcf;}
  .badge{position:absolute;left:270px;top:14px;width:88px;height:88px;border-radius:6px;background:var(--navy);}
  .tagline{
    position:absolute;left:388px;top:16px;margin:0;
    color:var(--white);font-weight:600;font-size:21px;line-height:22px;
  }
  .headline{
    position:absolute;left:0;width:600px;top:158px;
    text-align:center;color:var(--white);margin:0;
  }
  .headline .lead{display:block;font-weight:700;font-size:27px;line-height:34px;}
  .headline .big{
    display:block;font-style:italic;font-weight:900;font-size:57px;line-height:60px;
    letter-spacing:-1px;
    text-shadow:3px 3px 0 var(--blue-mid),-2px -2px 0 var(--sky-bright),2px -2px 0 var(--sky-bright),-2px 2px 0 var(--sky-bright);
  }
  .headline .last{display:block;font-style:italic;font-weight:800;font-size:46px;line-height:56px;letter-spacing:3px;}
  .phone{
    position:absolute;left:48px;top:728px;
    display:flex;align-items:center;gap:6px;
    font-family:"Oswald",sans-serif;font-weight:600;font-size:31px;color:var(--white);
  }
  .contact{
    position:absolute;left:300px;top:733px;
    list-style:none;margin:0;padding:0;
    color:var(--white);font-style:italic;font-weight:700;font-size:13.5px;line-height:19px;
  }
  .contact li{display:flex;align-items:center;gap:7px;}
  .contact .dot{width:10px;height:10px;border-radius:50%;background:var(--sky-soft);}
</style>
</head>
<body>
<div class="ad-frame">
<div class="ad">
  <svg class="backdrop" width="600" height="792" viewBox="0 0 600 792">
    <defs>
      <radialGradient id="weave" cx="70%" cy="55%" r="75%">
        <stop offset="0" stop-color="#2d5fae"/>
        <stop offset=".55" stop-color="#143d85"/>
        <stop offset="1" stop-color="#081f52"/>
      </radialGradient>
      <linearGradient id="topBlock" x1="0" y1="0" x2="1" y2="0">
        <stop offset="0" stop-color="#0677ba"/>
        <stop offset="1" stop-color="#0094d4"/>
      </linearGradient>
      <linearGradient id="interior" x1="0" y1="0" x2="1" y2="1">
        <stop offset="0" stop-color="#e9ecef"/>
        <stop offset=".5" stop-color="#b9bec4"/>
        <stop offset="1" stop-color="#6d7279"/>
      </linearGradient>
      <linearGradient id="sunset" x1="0" y1="0" x2="0" y2="1">
        <stop offset="0" stop-color="#e9c38a"/>
        <stop offset=".45" stop-color="#a08a74"/>
        <stop offset="1" stop-color="#5a4a2e"/>
      </linearGradient>
      <linearGradient id="silver" x1="0" y1="0" x2="1" y2="1">
        <stop offset="0" stop-color="#ffffff"/>
        <stop offset=".5" stop-color="#9aa4b0"/>
        <stop offset="1" stop-color="#e7ecf1"/>
      </linearGradient>
    </defs>
    <polygon class="top-block" points="330,0 600,0 600,62 360,84" fill="url(#topBlock)"/>
    <polygon points="580,62 600,62 600,72 380,92 390,84" fill="#6fccea"/>
    <polygon points="0,168 600,70 600,440 0,470" fill="url(#weave)" role="img" aria-label="Dark blue woven composite texture"/>
    <polygon points="0,470 250,480 0,505" fill="#0094d4"/>
    <polygon points="600,440 600,500 520,445" fill="#ffffff"/>
    <polygon points="0,522 345,480 345,700 0,735" fill="url(#interior)" role="img" aria-label="Caravan interior photos: kitchen, cabinets, bed and seating"/>
    <g stroke="#ffffff" stroke-width="4">
      <line x1="182" y1="505" x2="182" y2="717"/>
      <line x1="0" y1="630" x2="345" y2="595"/>
    </g>
    <polygon points="420,440 575,478 588,640 505,710 355,670 342,520" fill="url(#silver)"/>
    <polygon points="424,452 565,486 576,634 500,698 364,661 352,526" fill="url(#sunset)" role="img" aria-label="Fibreglass caravan with awning parked by the water at sunset"/>
    <polygon points="0,725 600,690 600,792 0,792" fill="#0094d4"/>
    <polygon points="530,640 600,610 600,700 560,702" fill="#0677ba"/>
  </svg>

  <div class="brand">
    <span class="brand-mark"></span>
    <p class="brand-name">BLUEGUM<br>TRAILERS</p>
  </div>
  <div class="divider"></div>
  <div class="badge" role="img" aria-label="Made in Australia certification badge"></div>
  <p class="tagline">locally<br>manufactured.</p>

  <h1 class="headline">
    <span class="lead">WE SPECIALISE IN</span>
    <span class="big">LIGHT WEIGHT</span>
    <span class="big">FIBREGLASS</span>
    <span class="big">COMPOSITE</span>
    <span class="last">CARAVANS</span>
  </h1>

  <div class="phone">
    <svg width="22" height="26" viewBox="0 0 24 24" aria-hidden="true"><path fill="#6fccea" d="M6.6 10.8a15.1 15.1 0 0 0 6.6 6.6l2.2-2.2c.3-.3.7-.4 1-.2 1.1.4 2.3.6 3.6.6.6 0 1 .4 1 1V20c0 .6-.4 1-1 1A17 17 0 0 1 3 4c0-.6.4-1 1-1h3.5c.6 0 1 .4 1 1 0 1.3.2 2.5.6 3.6.1.3 0 .7-.2 1z"/></svg>
    <span>(07) 3100 4821</span>
  </div>
  <ul class="contact">
    <li><span class="dot"></span>info@bluegumtrailers.com.au</li>
    <li><span class="dot"></span>www.bluegumtrailers.com.au</li>
  </ul>
</div>
</div>
</body>
</html>
```